Expense Tracker App for Young Adults

I need a mobile app designer to design an app UI for me. It is for an expense tracker app. I’ve attached a mind map of the various screens and features of the app.

I would like to see designs for this app which is targeted towards young adults (late teens & early 20s) just starting their career who want to plan their budgets and track their expenses.
Updates

Hello designers! I'm conscious that this is not a guaranteed project, so I can understand that some of you might be apprehensive. Just wanted to let you know that I'm willing to see your initial drafts that show your direction and theme for design. You don't have to design the whole app. In fact, it's better if you share your initial design ideas so that we can have a discussion and I can give my input. If I see some good initial designs, I will be happy to make this a guaranteed project. I'm simply being cautious since I'm bootstrapping this and funding out of my own pocket. Thank you for your understanding!

Target Market(s)

Young adults who are just starting their careers, late teens and early 20s.

Font styles to use
Sans Serif

Requirements
Must have
• Ease of use, smart and sleek, a guided setup wizard which will help users setup their account after signing up.
Should not have
• Clunky

```html
<!DOCTYPE html>
<html lang="en">
<head>
<meta charset="utf-8">
<title>KIRA - PX app screens</title>
<link href="https://fonts.googleapis.com/css2?family=Lato:wght@400;700;900&display=swap" rel="stylesheet">
<style>
:root{
  --page:#2a2a2a;
  --blue:#1a6fc0;
  --blue-deep:#1559a3;
  --yellow:#fbbf2e;
  --white:#ffffff;
  --ink:#2f2f2f;
  --muted:#555555;
  --line:#9a9a9a;
}
*{box-sizing:border-box;margin:0;padding:0}
html,body{width:724px;height:1200px;overflow:hidden;background:var(--page);font-family:'Lato',sans-serif;color:var(--ink)}
.board{position:relative;width:724px;height:1200px}
.screen{position:absolute;width:326px;height:556px;overflow:hidden;background:#eef0f3}
.screen--login{left:24px;top:27px}
.screen--signup{left:376px;top:27px}
.screen--list{left:24px;top:607px}
.screen--dated{left:376px;top:607px}
.scene{position:absolute;inset:0;background:linear-gradient(135deg,var(--yellow) 0%,var(--yellow) 22%,var(--blue) 22.5%,var(--blue-deep) 100%)}
.scene-band{position:absolute;left:0;right:0;height:110px;background:linear-gradient(90deg,#f4f4f4,#e8e8e8)}
.app-name{position:absolute;top:40px;left:0;right:0;text-align:center;font-weight:900;font-size:32px;color:var(--white);letter-spacing:0.5px}
.back-link{position:absolute;top:32px;right:11px;color:var(--white);font-weight:700;font-size:10px;display:flex;align-items:center;gap:3px}
.card{position:absolute;left:11px;width:304px;top:129px;background:var(--white);border-radius:8px;padding:0 18px}
.card--login{height:324px}
.card--signup{height:389px}
.card--tall{height:440px;border-radius:8px 8px 0 0}
.card-title{text-align:center;font-weight:700;font-size:18px;color:var(--ink);margin-top:34px}
.field{height:35px;border:1px solid var(--line);display:flex;align-items:center;padding:0 12px;font-size:11px;color:var(--ink)}
.btn-primary{height:35px;background:var(--yellow);color:var(--white);font-weight:700;font-size:15px;display:flex;align-items:center;justify-content:center}
.forgot{text-align:right;font-size:11px;color:var(--muted);margin:10px -1px 0 0}
.account-switch{text-align:center;font-size:12px;margin-top:22px}
.account-switch a{color:var(--blue);text-decoration:none}
.social-caption{text-align:center;font-size:12px;color:var(--ink);margin-top:31px}
.social-row{display:flex;justify-content:center;gap:20px;margin-top:12px}
.social-dot{width:12px;height:12px;border-radius:50%;background:var(--blue)}
.expense{display:flex;align-items:center;justify-content:space-between;background:var(--white);border-left:4px solid var(--yellow);box-shadow:0 1px 6px rgba(0,0,0,.12);padding:0 15px 0 12px}
.expense-heading{color:var(--blue);font-weight:700;font-size:11.5px}
.expense-category{font-size:10px;color:var(--ink);margin-top:3px}
.expense-date{font-size:11px;color:var(--ink);margin-bottom:3px}
.expense-amount{color:var(--yellow);font-size:14px}
.list .expense{height:54px;margin-bottom:21px}
.btn-secondary{display:block;width:85px;height:30px;margin:0 auto;background:var(--blue);color:var(--white);font-weight:700;font-size:11px;display:flex;align-items:center;justify-content:center;border-radius:2px}
.sorters{display:flex;gap:9px;margin-top:22px}
.sorter{width:83px}
.sorter-label{color:var(--blue);font-weight:700;font-size:11px;margin-bottom:7px}
.sorter-select{height:27px;border:1px solid #c8c8c8;display:flex;align-items:center;justify-content:space-between;padding:0 9px;font-size:10px}
.dated-list{margin-top:18px}
.dated-list .expense{height:69px;margin-bottom:15px}
.scroll-thumb{position:absolute;right:15px;top:203px;width:4px;height:27px;background:var(--blue)}
</style>
</head>
<body>
<main class="board">

  <section class="screen screen--login">
    <div class="scene" role="img" aria-label="Header illustration of a person presenting finance charts on a large screen"></div>
    <div class="app-name">KIRA - PX</div>
    <div class="card card--login">
      <h1 class="card-title">Login</h1>
      <div class="field" style="margin-top:26px">Username</div>
      <div class="field" style="margin-top:10px">Password</div>
      <p class="forgot">Forget Password?</p>
      <div class="btn-primary" style="margin-top:12px">Login</div>
      <p class="account-switch">Don't have an account? | <a href="#">Sign Up</a></p>
    </div>
  </section>

  <section class="screen screen--signup">
    <div class="scene" role="img" aria-label="Header illustration of a person presenting finance charts on a large screen"></div>
    <div class="app-name">KIRA - PX</div>
    <div class="card card--signup">
      <h1 class="card-title">Create an Account</h1>
      <div class="field" style="margin-top:21px">Full Name</div>
      <div class="field" style="margin-top:9px">Email Address</div>
      <div class="field" style="margin-top:9px">Create Password</div>
      <div class="field" style="margin-top:9px">Repeat Password</div>
      <div class="btn-primary" style="margin-top:10px">Login</div>
      <p class="social-caption">Or Sign Up with</p>
      <div class="social-row">
        <span class="social-dot" aria-label="Social sign up option one"></span>
        <span class="social-dot" aria-label="Social sign up option two"></span>
        <span class="social-dot" aria-label="Social sign up option three"></span>
      </div>
    </div>
  </section>

  <section class="screen screen--list">
    <div class="scene" role="img" aria-label="Header illustration of a person presenting finance charts on a large screen"></div>
    <div class="app-name">KIRA - PX</div>
    <div class="back-link"><svg width="6" height="8" viewBox="0 0 6 8"><path d="M5 1L2 4l3 3" stroke="#fff" stroke-width="1.5" fill="none"/></svg>Back</div>
    <div class="card card--tall list">
      <h1 class="card-title" style="margin-top:22px;font-size:19px">View Expenses</h1>
      <div style="margin-top:18px">
        <div class="expense"><div><div class="expense-heading">Expense Heading</div><div class="expense-category">Category Name</div></div><div class="expense-amount">$1,200</div></div>
        <div class="expense"><div><div class="expense-heading">Expense Heading</div><div class="expense-category">Category Name</div></div><div class="expense-amount">$1,200</div></div>
        <div class="expense"><div><div class="expense-heading">Expense Heading</div><div class="expense-category">Category Name</div></div><div class="expense-amount">$1,200</div></div>
        <div class="expense"><div><div class="expense-heading">Expense Heading</div><div class="expense-category">Category Name</div></div><div class="expense-amount">$1,200</div></div>
        <div class="expense"><div><div class="expense-heading">Expense Heading</div><div class="expense-category">Category Name</div></div><div class="expense-amount">$1,200</div></div>
      </div>
      <div class="btn-secondary" style="margin-top:-9px">Load More</div>
    </div>
  </section>

  <section class="screen screen--dated">
    <div class="scene" role="img" aria-label="Header illustration of a person presenting finance charts on a large screen"></div>
    <div class="app-name">KIRA - PX</div>
    <div class="back-link"><svg width="6" height="8" viewBox="0 0 6 8"><path d="M5 1L2 4l3 3" stroke="#fff" stroke-width="1.5" fill="none"/></svg>Back</div>
    <div class="card card--tall">
      <h1 class="card-title" style="margin-top:22px;font-size:19px">View Expenses by Date</h1>
      <div class="sorters">
        <div class="sorter"><div class="sorter-label">Sort by</div><div class="sorter-select">Amount<svg width="7" height="5" viewBox="0 0 7 5"><path d="M1 1l2.5 2.5L6 1" stroke="#333" fill="none"/></svg></div></div>
        <div class="sorter"><div class="sorter-label">Sort by</div><div class="sorter-select">Category<svg width="7" height="5" viewBox="0 0 7 5"><path d="M1 1l2.5 2.5L6 1" stroke="#333" fill="none"/></svg></div></div>
        <div class="sorter"><div class="sorter-label">Sort by</div><div class="sorter-select">Date<svg width="7" height="5" viewBox="0 0 7 5"><path d="M1 1l2.5 2.5L6 1" stroke="#333" fill="none"/></svg></div></div>
      </div>
      <div class="dated-list">
        <div class="expense"><div><div class="expense-date">Sep- 15-2020</div><div class="expense-heading">Expense Heading</div><div class="expense-category">Category Name</div></div><div class="expense-amount">$1,200</div></div>
        <div class="expense"><div><div class="expense-date">Sep- 15-2020</div><div class="expense-heading">Expense Heading</div><div class="expense-category">Category Name</div></div><div class="expense-amount">$1,200</div></div>
        <div class="expense"><div><div class="expense-date">Sep- 15-2020</div><div class="expense-heading">Expense Heading</div><div class="expense-category">Category Name</div></div><div class="expense-amount">$1,200</div></div>
        <div class="expense"><div><div class="expense-date">Sep- 15-2020</div><div class="expense-heading">Expense Heading</div><div class="expense-category">Category Name</div></div><div class="expense-amount">$1,200</div></div>
      </div>
    </div>
    <div class="scroll-thumb"></div>
  </section>

</main>
</body>
</html>
```